Animal Charity
Wrenfold
Animal Charity -
Simple
Ms Helena Crouch
Head of Communications and Fundraising
Hazel Mead Brackenford Corshire EX19 4TN
mon.varley@kestrelnet-mail.com
Name of Charity - Wrenfold Animal Rescue. Logo on businesscard should be based around a Wrenfold pole but the essence of the name Wrenfold is that the animals help humans as the charity involves rescuing Animals who then go on to help people in society. i.e represents the animal spirits helping the native americans in the representationof the pole.

```html
<!DOCTYPE html>
<html lang="en">
<head>
<meta charset="utf-8">
<title>Wrenfold Animal Rescue – Business Card</title>
<link rel="stylesheet" href="https://fonts.googleapis.com/css2?family=Arimo:wght@400&family=Tinos:wght@400&display=swap">
<style>
  :root {
    --card-light: #d6d6d6;
    --card-mid: #c8c8c8;
    --card-dark: #b9b9b9;
    --brand-red: #e3101b;
    --ink-grey: #4a4a4a;
    --ink-dark: #2f2f2f;
  }
  * { margin: 0; padding: 0; box-sizing: border-box; }
  html, body { width: 1200px; height: 660px; overflow: hidden; }
  .card {
    position: relative;
    width: 1200px;
    height: 660px;
    background: radial-gradient(ellipse at 55% 40%, var(--card-light) 0%, var(--card-mid) 60%, var(--card-dark) 100%);
    font-family: "Tinos", "Times New Roman", serif;
  }
  .brand {
    position: absolute;
    left: 70px;
    top: 262px;
    display: flex;
    align-items: center;
    gap: 34px;
    color: var(--ink-grey);
    font-family: "Arimo", Arial, sans-serif;
    font-weight: 400;
  }
  .brand-dot {
    width: 110px;
    height: 110px;
    border-radius: 50%;
    background: var(--brand-red);
    flex: none;
  }
  .brand-name { font-size: 80px; line-height: 0.95; letter-spacing: -1px; }
  .brand-name span { display: block; font-size: 30px; letter-spacing: 2px; margin-top: 14px; text-transform: uppercase; }
  .divider {
    position: absolute;
    left: 586px;
    top: 96px;
    width: 4px;
    height: 146px;
    background: var(--brand-red);
  }
  .person-name {
    position: absolute;
    left: 608px;
    top: 104px;
    font-size: 52px;
    font-weight: 400;
    color: var(--brand-red);
    line-height: 1;
  }
  .person-role {
    position: absolute;
    left: 608px;
    top: 172px;
    font-family: "Arimo", Arial, sans-serif;
    font-size: 30px;
    color: var(--ink-grey);
    line-height: 1;
  }
  .address {
    position: absolute;
    left: 648px;
    top: 290px;
    font-style: normal;
    font-size: 36px;
    line-height: 43px;
    color: var(--brand-red);
  }
  .contact {
    position: absolute;
    left: 648px;
    top: 478px;
    color: var(--ink-dark);
    list-style: none;
  }
  .contact li { display: flex; align-items: baseline; height: 42px; }
  .contact-label {
    width: 144px;
    font-size: 22px;
    letter-spacing: 1px;
    text-transform: uppercase;
  }
  .contact-value { font-size: 31px; letter-spacing: 1px; }
  .contact li.email .contact-label { width: 103px; text-transform: none; font-size: 28px; letter-spacing: 0; }
  .contact li.email .contact-value { font-size: 27px; letter-spacing: 0; }
</style>
</head>
<body>
  <div class="card">
    <div class="brand">
      <div class="brand-dot"></div>
      <div class="brand-name">Wrenfold<span>Animal Rescue</span></div>
    </div>

    <div class="divider"></div>
    <h1 class="person-name">Ms. Helena Crouch</h1>
    <p class="person-role">Communications / Fundraising</p>

    <address class="address">
      Hazel Mead<br>
      Brackenford<br>
      Corshire<br>
      EX19&nbsp;&nbsp;4TN
    </address>

    <ul class="contact">
      <li><span class="contact-label">Toll-free</span><span class="contact-value">07700 914362</span></li>
      <li><span class="contact-label">Phone</span><span class="contact-value">01632 960587</span></li>
      <li class="email"><span class="contact-label">email</span><span class="contact-value">mon.varley@kestrelnet-mail.com</span></li>
    </ul>
  </div>
</body>
</html>
```